Business Card Design

I am an Event and Wedding Planner in need of an eye catching business card featuring my logo (attached), my contact details, and my company tagline (Making each one of your gatherings radiant...) I would like the tagline in font similar the logo's font.
Updates
I have just noticed that my logo has a misspelling so for the final design, I will be uploading a corrected logo as soon as I have it.
My apologies.
Reason: Waiting on a corrected logo...Occasions is misspelled and it should say Weddings not Wedding
The logo has been corrected so now Occasions is spelled correctly and it says Weddings instead of Wedding. Please use Edwardian Script ITC as the font for the tagline so it will match the logo. Thank you for your patience.
Target Market(s)
Engaged couples and people hosting milestone celebrations. 25-50 years old, predominately female
Industry/Entity Type
Business
Contact Information for Business Card
Delphine Marsh, Event Manager / Owner, Mobile: 0491 836 254, Email: delphine@radiantgatheringsco.com.au, www.radiantgatheringsco.com.au, Making each one of your gatherings radiant...

```html
<!DOCTYPE html>
<html lang="en">
<head>
<meta charset="utf-8">
<title>Radiant Gatherings – Business Card</title>
<link rel="stylesheet" href="https://fonts.googleapis.com/css2?family=Pinyon+Script&family=Roboto+Condensed:wght@300;400;700&display=swap">
<style>
  :root {
    --backdrop: #e9e6e1;
    --card: #ffffff;
    --ink: #111111;
    --band: #0d0d0d;
    --band-text: #ffffff;
    --accent: #c8414b;
    --rule: #9a9a9a;
    --shadow: rgba(0, 0, 0, 0.18);
  }
  * { box-sizing: border-box; margin: 0; padding: 0; }
  html, body {
    width: 1200px; height: 894px; overflow: hidden;
    background: var(--backdrop);
    font-family: "Roboto Condensed", "Arial Narrow", sans-serif;
    color: var(--ink);
  }
  .canvas { position: relative; width: 1200px; height: 894px; }
  .card {
    position: absolute; left: 300px;
    width: 600px; height: 343px;
    background: var(--card);
    border-radius: 22px;
    overflow: hidden;
    box-shadow: 0 10px 28px var(--shadow);
  }
  .card--back { top: 64px; }
  .card--front { top: 487px; }

  /* Brand name block */
  .brand {
    position: absolute;
    display: flex; flex-direction: column; align-items: flex-start;
  }
  .brand__row { display: flex; align-items: center; gap: 10px; }
  .brand__name {
    font-weight: 300; color: var(--ink); letter-spacing: 0.5px;
    white-space: nowrap; line-height: 1.1;
  }
  .brand__dot { border-radius: 50%; background: var(--accent); flex: none; }
  .brand__rule { height: 1px; background: var(--rule); margin-top: 6px; }
  .tagline {
    font-family: "Pinyon Script", "Edwardian Script ITC", cursive;
    color: var(--ink); white-space: nowrap; line-height: 1.2;
  }

  .card--back .brand { left: 50%; top: 50%; transform: translate(-50%, -50%); }
  .card--back .brand__name { font-size: 44px; }
  .card--back .brand__dot { width: 18px; height: 18px; }
  .card--back .brand__rule { width: 300px; margin-left: 30px; }
  .card--back .tagline { font-size: 26px; margin: 8px 0 0 30px; }

  .card--front .brand { left: 48px; top: 26px; }
  .card--front .brand__name { font-size: 34px; }
  .card--front .brand__dot { width: 14px; height: 14px; }
  .card--front .brand__rule { width: 230px; margin-left: 24px; }
  .card--front .tagline { font-size: 19px; margin: 4px 0 0 24px; }

  /* Name plate */
  .nameplate {
    position: absolute; left: 0; top: 134px;
    width: 312px; height: 44px;
    background: var(--band); color: var(--band-text);
    border-radius: 0 22px 22px 0;
    padding: 5px 0 0 30px;
  }
  .nameplate__name {
    font-weight: 700; font-size: 17px; letter-spacing: 1px; line-height: 18px;
    text-transform: uppercase;
  }
  .nameplate__role {
    font-weight: 300; font-size: 12px; letter-spacing: 1px; line-height: 15px;
    text-transform: uppercase;
  }

  /* Contact list */
  .contacts {
    position: absolute; left: 170px; top: 192px;
    list-style: none;
    font-size: 13px; font-weight: 400; letter-spacing: 0.8px;
    text-transform: uppercase; line-height: 17px;
  }
  .contacts li { display: flex; align-items: flex-start; gap: 9px; }
  .contacts svg { width: 13px; height: 13px; margin-top: 2px; flex: none; }

  /* Bottom band */
  .footer-band {
    position: absolute; left: 176px; right: 0; bottom: 0;
    height: 30px; background: var(--band);
    border-radius: 15px 0 0 0;
  }
</style>
</head>
<body>
<main class="canvas">

  <section class="card card--back" aria-label="Business card, back">
    <div class="brand">
      <div class="brand__row">
        <span class="brand__name">Radiant Gatherings</span>
        <span class="brand__dot"></span>
      </div>
      <div class="brand__rule"></div>
      <p class="tagline">Making each one of your gatherings radiant...</p>
    </div>
  </section>

  <section class="card card--front" aria-label="Business card, front">
    <div class="brand">
      <div class="brand__row">
        <span class="brand__name">Radiant Gatherings</span>
        <span class="brand__dot"></span>
      </div>
      <div class="brand__rule"></div>
      <p class="tagline">Making each one of your gatherings radiant...</p>
    </div>

    <div class="nameplate">
      <p class="nameplate__name">Delphine Marsh</p>
      <p class="nameplate__role">Event Manager / Owner</p>
    </div>

    <ul class="contacts">
      <li>
        <svg viewBox="0 0 16 16" aria-hidden="true"><circle cx="8" cy="8" r="7.2" fill="none" stroke="#111" stroke-width="1.4"/><path d="M5.2 4.4l1.6-.4.8 2-1 .7c.4 1 1.2 1.8 2.2 2.2l.7-1 2 .8-.4 1.6c-3.2.2-6.1-2.7-5.9-5.9z" fill="#111"/></svg>
        <span>0491 836 254</span>
      </li>
      <li>
        <svg viewBox="0 0 16 16" aria-hidden="true"><circle cx="8" cy="8" r="7.2" fill="none" stroke="#111" stroke-width="1.4"/><path d="M4.8 5.6a1.6 1.6 0 0 1 1.6-1.4h3.2a1.6 1.6 0 0 1 1.6 1.4v.8H9.6v-.6H6.4v.6H4.8z M6 7h4l1.6 4.6H4.4z" fill="#111"/></svg>
        <span>(02) 9381 4406</span>
      </li>
      <li>
        <svg viewBox="0 0 16 16" aria-hidden="true"><circle cx="8" cy="8" r="7.2" fill="none" stroke="#111" stroke-width="1.4"/><rect x="4.2" y="5.2" width="7.6" height="5.6" fill="#111"/><path d="M4.4 5.4L8 8.4l3.6-3" fill="none" stroke="#fff" stroke-width="0.9"/></svg>
        <span>delphine@radiantgatheringsco.com.au</span>
      </li>
      <li>
        <svg viewBox="0 0 16 16" aria-hidden="true"><circle cx="8" cy="8" r="7.2" fill="#111"/><g fill="none" stroke="#fff" stroke-width="0.9"><circle cx="8" cy="8" r="4.2"/><ellipse cx="8" cy="8" rx="1.8" ry="4.2"/><path d="M3.8 8h8.4"/></g></svg>
        <span>www.radiantgatheringsco.com.au</span>
      </li>
      <li>
        <svg viewBox="0 0 16 16" aria-hidden="true"><circle cx="8" cy="8" r="7.2" fill="#111"/><path d="M8 3.6a2.9 2.9 0 0 1 2.9 2.9C10.9 8.8 8 12.4 8 12.4S5.1 8.8 5.1 6.5A2.9 2.9 0 0 1 8 3.6z" fill="#fff"/><circle cx="8" cy="6.5" r="1.1" fill="#111"/></svg>
        <span>18 Harbourview Lane,<br>Sydney NSW, Australia</span>
      </li>
    </ul>

    <div class="footer-band"></div>
  </section>

</main>
</body>
</html>
```